Business card design needed

We design, manufacture and install kitchen robes vanity etc.
We have a current card that i want to upload that you can base the design around and make suggestions for other design but we need the logo to be unchanged that i will up load along with our current card.

Industry/Entity Type

Business

Contact Information for Business Card

Marlowe Cabinet Studio
Daniel Ferricott
27 Brindlemere Avenue, Harwick S.A 5082
daniel@marlowecabinet.com.au
Lic. No. Bld 274958 Bld 291436

```html
<!DOCTYPE html>
<html lang="en">
<head>
<meta charset="utf-8">
<title>Marlowe Cabinet Studio — Business Card</title>
<link rel="stylesheet" href="https://fonts.googleapis.com/css2?family=Open+Sans:wght@400;600&display=swap">
<style>
  :root {
    --backdrop: #000000;
    --card: #ffffff;
    --card-edge: #8a8a8a;
    --green: #6f9a3a;
    --grey: #7d7d7d;
    --grey-dark: #6a6a6a;
  }
  * { margin: 0; padding: 0; box-sizing: border-box; }
  html, body {
    width: 1200px;
    height: 1112px;
    overflow: hidden;
    background: var(--backdrop);
    font-family: "Open Sans", sans-serif;
  }
  .canvas { position: relative; width: 1200px; height: 1112px; }

  .card {
    position: absolute;
    left: 91px;
    width: 1010px;
    background: var(--card);
    border: 4px solid var(--card-edge);
  }
  .card--front { top: 51px; height: 486px; }
  .card--back  { top: 572px; height: 484px; }

  .card > * { position: absolute; }

  /* Front */
  .licence { left: 64px; top: 56px; font-size: 23px; color: var(--green); }
  .person-name { right: 32px; top: 54px; font-size: 37px; color: var(--green); }
  .person-email { right: 32px; top: 116px; font-size: 22px; color: var(--grey); }

  .brand { display: flex; align-items: center; gap: 14px; white-space: nowrap; }
  .brand__mark { width: 22px; height: 22px; background: var(--green); }
  .brand__name { font-weight: 600; color: var(--grey); text-transform: uppercase; letter-spacing: 0.5px; }
  .card--front .brand { left: 48px; top: 300px; }
  .card--front .brand__name { font-size: 31px; }

  .rule { height: 5px; background: var(--green); }
  .card--front .rule { left: 46px; right: 43px; top: 387px; }
  .address { left: 46px; top: 412px; font-size: 29px; color: var(--grey); }

  /* Back */
  .card--back .brand { left: 40px; top: 100px; }
  .card--back .brand__mark { width: 16px; height: 16px; }
  .card--back .brand__name { font-size: 21px; }
  .tagline { right: 41px; top: 38px; font-size: 37px; color: var(--grey-dark); }
  .card--back .rule { left: 351px; right: 41px; top: 92px; }

  .service {
    transform: translate(-50%, -50%);
    font-size: 24px;
    text-transform: uppercase;
    white-space: nowrap;
  }
  .service--green { color: var(--green); }
  .service--grey { color: var(--grey); }
</style>
</head>
<body>
<div class="canvas">

  <section class="card card--front">
    <p class="licence">Lic. No. Bld 274958, Bld 291436</p>
    <p class="person-name">Daniel Ferricott</p>
    <p class="person-email">daniel@marlowecabinet.com.au</p>
    <div class="brand">
      <span class="brand__mark"></span>
      <span class="brand__name">Marlowe Cabinet Studio</span>
    </div>
    <div class="rule"></div>
    <p class="address">27 Brindlemere Avenue, Harwick S.A 5082</p>
  </section>

  <section class="card card--back">
    <div class="brand">
      <span class="brand__mark"></span>
      <span class="brand__name">Marlowe Cabinet Studio</span>
    </div>
    <p class="tagline">Custom Made</p>
    <div class="rule"></div>
    <p class="service service--green" style="left:521px; top:194px;">Robes</p>
    <p class="service service--grey"  style="left:243px; top:247px;">Kitchen</p>
    <p class="service service--grey"  style="left:806px; top:238px;">Laundry</p>
    <p class="service service--grey"  style="left:501px; top:320px;">Entertainment Units</p>
    <p class="service service--green" style="left:150px; top:376px;">Vanities</p>
    <p class="service service--green" style="left:862px; top:376px;">Flat Packs</p>
  </section>

</div>
</body>
</html>
```